Infographic for Digital Marketing Agency

Infographic or one pager a presentation on a page and a presentation (PowerPoint presentation). We need to represent our "Hidden Growth Recipe" with our Marketing Process Plan (5 steps plan and list of our services) and the "Sales funnel" process (see draft attached). Specifications: - We would like to have a graphic up-to-date, modern, dynamic chart related to the digital marketing industry. - For the Hidden Recipe and the design of our "5 Steps", see the file Infographic-Hidden Recipe_Content & Infographic-Plan 5 Steps_Content) for the content to be added - and for the Channel Marketing (Funnel Marketing) please see the example attached (file: Infographic-Sales funnel_example) to see the content and the concept (strategies) but do not copy the same design. Need another kind of design to reprocess the flow chart. You can do one big Infographic to represent the 3 or 3 files: - The Hidden Recipe of the Web marketing (Hidden Recipe) - The marketing plan in 5 steps (5 steps plan) - The sales channel (the sales funnel process) See 3 documents attached for the content (and see notes in the documents) and our Logo. Our brand must be on all documents. And I'm looking for: https://www.vimbrelo.ca/equipequorva/marketing/ I really like this kind of flow chart: https://www.vimbrelo.ca/pin/918274650193847261/ Content has to be in English on all my designs. Also, all the designs must fit our brand. Http://www.quorva.ca/ You can use our Website images if you need. Designers can provide other suggestions. And please ask questions if not sure about what I am expected. I also have some others projects coming. Thanks. Gaspard qOrva

Target Market(s)

Marketing director, VP of sales and marketing, Entrepreneurs, Professionals on Health industry, Real estate people

Industry/Entity Type

Marketing

Font styles to use
Sans Serif

Colors

Designer to choose colors to be used in the design.

Requirements
Must have
• Must be in French ... But I provide all the content in my files attached to the brief. Must be the same king of inspirations I provide on the brief. Need something really big in Digital Marketing industry.
Nice to have
• I am looking for: https://www.vimbrelo.ca/equipequorva/marketing/ I really like this kind of flow chart: https://www.vimbrelo.ca/pin/918274650193847261/
Should not have
• Funnel Flow Chart I provide. It's just to present the concept and Flow chart and my content so you can reproduce in a different way.

```html
<!DOCTYPE html>
<html lang="fr">
<head>
<meta charset="utf-8">
<title>qOrva – Infographie marketing web</title>
<link href="https://fonts.googleapis.com/css2?family=Oswald:wght@300;400;500;600;700&family=Roboto:wght@300;400;500;700&family=Roboto+Condensed:wght@300;400;700&display=swap" rel="stylesheet">
<style>
:root{
  --yellow:#f9c34a;
  --teal:#6fcdc4;
  --blue:#5fa4e6;
  --blue-deep:#3b8fd8;
  --green:#8cc63f;
  --teal-deep:#3bb6b0;
  --orange:#f7a04b;
  --gold:#f5b942;
  --coral:#e8553e;
  --ink:#262626;
  --grey:#6b6b6b;
  --line:#cfcfcf;
  --board:#378a2e;
  --pink:#f3a5b0;
  --paper:#ffffff;
  --device:#2b2f36;
}
*{box-sizing:border-box;margin:0;padding:0}
html,body{width:1200px;height:3651px;overflow:hidden;background:var(--paper)}
body{position:relative;font-family:"Roboto",Arial,sans-serif;color:var(--ink)}
.abs{position:absolute}

/* hero */
.hero{position:absolute;left:0;top:0;width:1200px;height:986px}
.hero svg{position:absolute;left:0;top:0}
.brand{position:absolute;left:0;width:1200px;top:92px;text-align:center}
.brand-name{font-family:"Oswald",sans-serif;font-weight:700;font-size:88px;line-height:1;letter-spacing:2px;color:#111}
.brand-tag{font-family:"Roboto Condensed",sans-serif;font-size:22px;color:#111;margin-top:4px;letter-spacing:.5px}
.badge{position:absolute;left:487px;top:263px;width:224px;height:72px;border:2px solid #d9d9d9;border-radius:6px;background:#fff}
.badge::before{content:"";position:absolute;left:18px;top:18px;width:34px;height:34px;border-radius:50%;background:#d0d0d0}
.badge::after{content:"";position:absolute;left:66px;top:24px;width:130px;height:22px;border-radius:4px;background:#ececec}
.hero-num{position:absolute;font-family:"Roboto",sans-serif;font-weight:300;font-size:64px;color:#fff;line-height:1}
.hero-title{position:absolute;color:#fff;line-height:1.02}
.hero-title .b{font-family:"Oswald",sans-serif;font-weight:600;display:block}
.hero-title .l{font-family:"Roboto Condensed",sans-serif;font-weight:300;display:block}
.t-formule{left:54px;top:455px}
.t-formule .b,.t-formule .l{font-size:60px}
.t-canal{right:54px;top:360px;text-align:right}
.t-canal .b{font-size:62px}
.t-canal .l{font-size:50px;letter-spacing:1px}
.t-plan{left:645px;top:722px}
.t-plan .b{font-size:62px}
.t-plan .l{font-size:54px}

.divider{position:absolute;left:0;width:1200px;border-top:3px dotted #bdbdbd}

/* formula */
.formula-head{position:absolute;left:365px;top:1071px;width:475px;height:146px}
.formula-head svg{position:absolute;left:0;top:0}
.fh-la{position:absolute;left:30px;top:6px;font-family:"Oswald",sans-serif;font-weight:700;font-size:108px;line-height:1;color:var(--green)}
.fh-top{position:absolute;left:150px;top:14px;font-family:"Oswald",sans-serif;font-weight:400;font-size:50px;line-height:1;color:var(--orange);letter-spacing:2px}
.fh-mid{position:absolute;left:150px;top:70px;font-family:"Roboto Condensed",sans-serif;font-weight:300;font-size:46px;line-height:1;color:var(--orange)}
.fh-sub{position:absolute;left:0;width:475px;top:116px;text-align:center;font-family:"Roboto",sans-serif;font-size:20px;letter-spacing:9px;color:var(--green)}

.card{position:absolute;top:1261px;width:227px;height:333px;background:#fff;box-shadow:0 4px 12px rgba(0,0,0,.18)}
.card-photo{height:175px;width:100%}
.card-label{height:158px;display:flex;align-items:center;justify-content:center;text-align:center;font-family:"Roboto",sans-serif;font-weight:500;font-size:24px;line-height:1.4;color:var(--ink)}
.op{position:absolute;top:1424px;width:34px;height:34px;border-radius:50%;background:#333;border:3px solid #fff;color:#fff;font:700 18px/28px "Roboto",sans-serif;text-align:center}
.timeline{position:absolute;left:170px;top:1598px;width:858px;height:8px;background:linear-gradient(90deg,var(--blue-deep),var(--green),var(--teal-deep),var(--gold))}
.dot{position:absolute;top:1573px;width:58px;height:58px;border-radius:50%;border:5px solid #fff;box-shadow:0 0 0 2px rgba(0,0,0,.06);color:#fff;font:500 28px/48px "Roboto",sans-serif;text-align:center}

/* plan */
.plan-title{position:absolute;left:0;width:1200px;top:1732px;text-align:center;font-family:"Oswald",sans-serif;font-weight:400;font-size:42px;letter-spacing:3px;color:var(--blue-deep)}
.plan-sub{position:absolute;left:0;width:1200px;top:1798px;text-align:center;font-family:"Roboto",sans-serif;font-weight:700;font-size:22px;color:var(--ink)}
.tag{position:absolute;top:1892px;height:30px;border-radius:3px;color:#fff;font:700 15px/30px "Roboto Condensed",sans-serif;letter-spacing:1.5px;text-align:center}
.step{position:absolute;top:1955px;width:205px}
.step-no{font-family:"Roboto Condensed",sans-serif;font-weight:700;font-size:18px;color:var(--ink);letter-spacing:.5px}
.step-cat{font-family:"Roboto Condensed",sans-serif;font-weight:400;font-size:17px;letter-spacing:2px;margin-top:4px}
.step-list{list-style:none;margin-top:16px;border-left:2px solid var(--line);padding-left:18px;display:flex;flex-direction:column;gap:12px}
.step-list li{position:relative;font-size:12.5px;line-height:1.35;color:var(--grey)}
.step-list li::before{content:"";position:absolute;left:-27px;top:2px;width:12px;height:12px;border-radius:50%;background:var(--c);border:2px solid #fff}
.step-1 .step-list{gap:28px}

/* funnel */
.banner{position:absolute;left:61px;top:2470px;width:1071px;height:61px;background:var(--orange);color:#fff;text-align:center;font:500 32px/61px "Oswald",sans-serif;letter-spacing:4px;box-shadow:0 4px 0 #d8843a}
.board{position:absolute;left:151px;top:2531px;width:900px;height:974px;background:var(--board)}
.board svg{position:absolute;left:0;top:0}
.board text{font-family:"Oswald",sans-serif;fill:#fff}

/* footer */
.footer{position:absolute;left:0;top:3590px;width:1200px;height:61px;background:repeating-linear-gradient(-45deg,var(--pink) 0 6px,#fff 6px 12px)}
.footer-url{position:absolute;left:0;width:1200px;top:3612px;text-align:center;font:500 20px/1 "Roboto",sans-serif;letter-spacing:12px;color:#3d4a66}
.footer-url span{background:#fff;padding:4px 14px}
</style>
</head>
<body>

<header class="hero">
  <svg width="1200" height="986" viewBox="0 0 1200 986">
    <rect width="1200" height="986" fill="#ffffff"/>
    <polygon points="0,0 350,0 600,520 0,940" fill="var(--yellow)"/>
    <polygon points="850,0 1200,0 1200,740 600,520" fill="var(--teal)"/>
    <polygon points="0,986 0,940 600,520 1200,740 1200,986" fill="var(--blue)"/>
    <g role="img" aria-label="Tablette et téléphone affichant un site web">
      <rect x="92" y="231" width="139" height="190" rx="10" fill="var(--device)"/>
      <rect x="102" y="243" width="119" height="164" fill="#e9f1fa"/>
      <rect x="60" y="330" width="62" height="108" rx="8" fill="var(--device)"/>
      <rect x="66" y="342" width="50" height="84" fill="#dfeaf5"/>
    </g>
    <g role="img" aria-label="Écran d'ordinateur affichant une page web">
      <rect x="900" y="506" width="232" height="150" rx="6" fill="var(--device)"/>
      <rect x="909" y="514" width="214" height="128" fill="#e4eef8"/>
      <rect x="996" y="656" width="40" height="18" fill="#9aa3ad"/>
      <rect x="970" y="674" width="92" height="7" rx="3" fill="#c4cad1"/>
    </g>
    <g role="img" aria-label="Écran, tablette et téléphone affichant un plan marketing">
      <rect x="390" y="705" width="170" height="130" rx="6" fill="var(--device)"/>
      <rect x="398" y="713" width="154" height="112" fill="#f2f5f8"/>
      <rect x="340" y="790" width="90" height="130" rx="8" fill="var(--device)"/>
      <rect x="347" y="800" width="76" height="108" fill="#e9eef3"/>
      <rect x="420" y="880" width="48" height="80" rx="6" fill="var(--device)"/>
      <rect x="425" y="888" width="38" height="62" fill="#e9eef3"/>
    </g>
  </svg>
  <div class="brand">
    <div class="brand-name">qOrva</div>
    <div class="brand-tag">Marketing Automatique</div>
  </div>
  <div class="badge" role="img" aria-label="Badge partenaire"></div>
  <div class="hero-num" style="left:495px;top:455px">1</div>
  <div class="hero-num" style="left:584px;top:540px">2</div>
  <div class="hero-num" style="left:672px;top:455px">3</div>
  <h2 class="hero-title t-formule"><span class="b">LA FORMULE</span><span class="l">SECRÈTE DU</span><span class="b">MARKETING WEB</span></h2>
  <h2 class="hero-title t-canal"><span class="b">LE CANAL</span><span class="l">MARKETING</span></h2>
  <h2 class="hero-title t-plan"><span class="b">LE PLAN</span><span class="l">MARKETING</span><span class="b">EN 5 ÉTAPES</span></h2>
</header>

<div class="divider" style="top:1017px"></div>

<section class="formula">
  <div class="formula-head">
    <svg width="475" height="146" viewBox="0 0 475 146" fill="none" stroke="var(--orange)" stroke-width="4">
      <path d="M2 40 V2 H60"/><path d="M415 2 H473 V40"/>
      <path d="M2 80 V104"/><path d="M473 80 V104"/>
    </svg>
    <div class="fh-la">LA</div>
    <div class="fh-top">FORMULE</div>
    <div class="fh-mid">SECRÈTE DU</div>
    <div class="fh-sub">MARKETING WEB</div>
  </div>

  <div class="card" style="left:58px">
    <div class="card-photo" role="img" aria-label="Photo : main sur une tablette" style="background:linear-gradient(135deg,#1d4f86,#3a8fd0 60%,#0f2c4d)"></div>
    <div class="card-label">+ Revenus /<br>Opportunités</div>
  </div>
  <div class="card" style="left:341px">
    <div class="card-photo" role="img" aria-label="Photo : personne au clavier d'un ordinateur portable" style="background:linear-gradient(135deg,#c9b8a6,#efe6dc 55%,#8f7d6b)"></div>
    <div class="card-label">Trafic<br>Web</div>
  </div>
  <div class="card" style="left:628px">
    <div class="card-photo" role="img" aria-label="Photo : réunion d'équipe au bureau" style="background:linear-gradient(135deg,#7d8a92,#cfd6da 55%,#5d6a70)"></div>
    <div class="card-label">%<br>Conversion</div>
  </div>
  <div class="card" style="left:915px">
    <div class="card-photo" role="img" aria-label="Photo : poignée de main entre gens d'affaires" style="background:linear-gradient(135deg,#e9e6e2,#b9b2aa 55%,#4a4a4a)"></div>
    <div class="card-label">Valeur<br>Client</div>
  </div>
  <div class="op" style="left:296px">=</div>
  <div class="op" style="left:582px">×</div>
  <div class="op" style="left:869px">×</div>

  <div class="timeline"></div>
  <div class="dot" style="left:141px;background:var(--blue-deep)">1</div>
  <div class="dot" style="left:426px;background:var(--green)">2</div>
  <div class="dot" style="left:713px;background:var(--teal-deep)">3</div>
  <div class="dot" style="left:999px;background:var(--gold)">4</div>
</section>

<div class="divider" style="top:1675px"></div>

<section class="plan">
  <h2 class="plan-title">LE PLAN MARKETING EN 5 ÉTAPES</h2>
  <p class="plan-sub">Donc… Voici les 5 étapes de votre plan à mettre en place!</p>
  <div class="tag" style="left:175px;width:165px;background:var(--orange)">IMPRESSIONS</div>
  <div class="tag" style="left:382px;width:158px;background:var(--green)">INCITATIF</div>
  <div class="tag" style="left:584px;width:171px;background:var(--teal-deep)">OFFRE IRRÉSISTIBLE</div>
  <div class="tag" style="left:808px;width:166px;background:var(--gold)">MAXIMISATION</div>

  <div class="step step-1" style="left:58px;--c:var(--coral)">
    <div class="step-no">ÉTAPE 1</div>
    <div class="step-cat" style="color:var(--coral)">POSITIONNEMENT</div>
    <ul class="step-list">
      <li>Boutique, micro site, site Web complet ou landing pages modernes et actuels.</li>
      <li>Analyse et structure d'indexation Chercheo &amp; Rapport de mots clés en lien avec vos produits / services.</li>
      <li>Programme de marketing automatique (Convertissez votre site Web en outil de vente.</li>
      <li>Marketing de contenu de présentation.</li>
    </ul>
  </div>
  <div class="step" style="left:282px;--c:var(--orange)">
    <div class="step-no">ÉTAPE 2</div>
    <div class="step-cat" style="color:var(--orange)">VISITEURS</div>
    <ul class="step-list">
      <li>Canal marketing visiteurs.</li>
      <li>Indexation Chercheo.</li>
      <li>Marketing de contenu récurrent. (Blogue)</li>
      <li>Répertoires d'affaires &amp; Référencement local.</li>
      <li>Publicité mobile.</li>
      <li>Publicité au coût par clic (PPC, Chercheo).</li>
      <li>Publicité médias sociaux (Amisphère, ProRéseau, VidéoFlux, Etc.)</li>
      <li>Publicité bannières Web (Display).</li>
      <li>(À venir) Marketing de ré-engagement.</li>
    </ul>
  </div>
  <div class="step" style="left:500px;--c:var(--green)">
    <div class="step-no">ÉTAPE 3</div>
    <div class="step-cat" style="color:var(--green)">PROSPECTS</div>
    <ul class="step-list">
      <li>Marketing de promotions prospects.</li>
      <li>Canal marketing prospects.</li>
      <li>Marketing de contenu prospects.</li>
      <li>Publicité remarketing prospects.</li>
      <li>Marketing médias sociaux.</li>
      <li>Référencement par liens externes.</li>
      <li>(À venir) Marketing de conférence Web (Webinaire)</li>
    </ul>
  </div>
  <div class="step" style="left:716px;--c:var(--teal-deep)">
    <div class="step-no">ÉTAPE 4</div>
    <div class="step-cat" style="color:var(--teal-deep)">OPPORTUNITÉS</div>
    <ul class="step-list">
      <li>Canal marketing satisfaction client.</li>
      <li>Canal marketing opportunités.</li>
      <li>Marketing de contenu clients. (Infolettre)</li>
      <li>Marketing de promotions clients.</li>
      <li>Création de produits Web (Complexe)</li>
      <li>Publicité Web et remarketing clients.</li>
    </ul>
  </div>
  <div class="step" style="left:952px;width:190px;--c:var(--orange)">
    <div class="step-no">ÉTAPE 5</div>
    <div class="step-cat" style="color:var(--orange)">PROMOTEURS</div>
    <ul class="step-list">
      <li>Marketing de contenu promoteurs.</li>
      <li>Marketing de références.</li>
      <li>Marketing d'affiliation.</li>
      <li>Publicité Web et remarketing promoteurs.</li>
    </ul>
  </div>

  <svg class="abs" style="left:870px;top:2200px" width="280" height="300" viewBox="0 0 280 300" role="img" aria-label="Tablette et téléphone affichant un article">
    <rect x="67" y="3" width="207" height="243" rx="12" fill="var(--device)"/>
    <rect x="79" y="17" width="183" height="215" fill="#f4f6f8"/>
    <rect x="11" y="137" width="80" height="158" rx="10" fill="var(--device)"/>
    <rect x="17" y="151" width="68" height="128" fill="#eef1f4"/>
  </svg>
</section>

<section class="funnel">
  <div class="banner">★ LE CANAL MARKETING ★</div>
  <div class="board">
    <svg width="900" height="974" viewBox="0 0 900 974" fill="none" stroke="#fff" stroke-width="2">
      <defs>
        <marker id="arrow" viewBox="0 0 10 10" refX="9" refY="5" markerWidth="7" markerHeight="7" orient="auto">
          <path d="M0 0 L10 5 L0 10 z" fill="#fff" stroke="none"/>
        </marker>
      </defs>

      <rect x="312" y="24" width="280" height="54"/>
      <text x="452" y="60" text-anchor="middle" font-size="23" font-weight="600" letter-spacing="4" stroke="none">MARCHÈ CIBLE</text>
      <path d="M312 51 H190 V160 H236" marker-end="url(#arrow)"/>
      <path d="M592 51 H715 V160 H666" marker-end="url(#arrow)"/>

      <rect x="238" y="134" width="426" height="53"/>
      <text x="451" y="169" text-anchor="middle" font-size="21" font-weight="600" letter-spacing="1" stroke="none">CHOISIR VOTRE SOURCE DE TRAFIC</text>

      <path d="M451 187 V231 M190 231 H701"/>
      <g>
        <path d="M190 231 V263 M275 231 V263 M360 231 V263 M445 231 V263 M530 231 V263 M616 231 V263 M701 231 V263" marker-end="url(#arrow)"/>
        <g fill="#fff" stroke="none" role="img" aria-label="Sources de trafic : réseaux sociaux, vidéo, blogue et moteurs de recherche">
          <circle cx="190" cy="282" r="17"/><circle cx="275" cy="282" r="17"/><circle cx="360" cy="282" r="17"/>
          <circle cx="445" cy="282" r="17"/><circle cx="530" cy="282" r="17"/><circle cx="616" cy="282" r="17"/>
          <circle cx="701" cy="282" r="17"/>
        </g>
        <path d="M190 299 V318 M275 299 V318 M360 299 V318 M445 299 V318 M530 299 V318 M616 299 V318 M701 299 V318 M190 318 H701"/>
        <path d="M451 318 V334" marker-end="url(#arrow)"/>
      </g>

      <rect x="307" y="336" width="290" height="62"/>
      <text x="452" y="364" text-anchor="middle" font-size="20" font-weight="600" stroke="none">OFFRIR UN INCITATIF</text>
      <text x="452" y="389" text-anchor="middle" font-size="14" stroke="none">⊕ OUI</text>
      <path d="M452 398 V440 H282 V478" marker-end="url(#arrow)"/>

      <!-- row 1 -->
      <rect x="136" y="480" width="292" height="56"/>
      <text x="282" y="503" text-anchor="middle" font-size="16" font-weight="600" stroke="none">OFFRIR UN OFFRE IRRÉSISTIBLE</text>
      <text x="282" y="527" text-anchor="middle" font-size="13" stroke="none">⊕ OUI    ⊖ NON</text>
      <rect x="494" y="480" width="268" height="56"/>
      <text x="628" y="503" text-anchor="middle" font-size="16" font-weight="600" stroke="none">COURRIELS AUTOMATIQUES</text>
      <text x="628" y="527" text-anchor="middle" font-size="13" stroke="none">⊕ OUI    ⊖ NON</text>
      <path d="M428 508 H492" marker-end="url(#arrow)"/>

      <!-- row 2 -->
      <path d="M282 536 V588" marker-end="url(#arrow)"/>
      <path d="M628 536 V563 H300 V588" marker-end="url(#arrow)"/>
      <rect x="136" y="590" width="292" height="56"/>
      <text x="282" y="613" text-anchor="middle" font-size="16" font-weight="600" stroke="none">OFFRIR VOTRE OFFRE PRINCIPALE</text>
      <text x="282" y="637" text-anchor="middle" font-size="13" stroke="none">⊕ OUI    ⊖ NON</text>
      <rect x="494" y="590" width="268" height="56"/>
      <text x="628" y="613" text-anchor="middle" font-size="16" font-weight="600" stroke="none">COURRIELS AUTOMATIQUES</text>
      <text x="628" y="637" text-anchor="middle" font-size="13" stroke="none">⊕ OUI    ⊖ NON</text>
      <path d="M428 618 H492" marker-end="url(#arrow)"/>

      <!-- row 3 -->
      <path d="M282 646 V698" marker-end="url(#arrow)"/>
      <path d="M628 646 V673 H300 V698" marker-end="url(#arrow)"/>
      <rect x="136" y="700" width="292" height="56"/>
      <text x="282" y="723" text-anchor="middle" font-size="16" font-weight="600" stroke="none">OFFRIR UNE OFFRE SUPPLÉMENTAIRE</text>
      <text x="282" y="747" text-anchor="middle" font-size="13" stroke="none">⊕ OUI    ⊖ NON</text>
      <rect x="494" y="700" width="268" height="56"/>
      <text x="628" y="723" text-anchor="middle" font-size="16" font-weight="600" stroke="none">COURRIELS AUTOMATIQUES</text>
      <text x="628" y="747" text-anchor="middle" font-size="13" stroke="none">⊕ OUI    ⊖ NON</text>
      <path d="M428 728 H492" marker-end="url(#arrow)"/>

      <!-- to remarketing -->
      <path d="M282 756 V800 H452 V845" marker-end="url(#arrow)"/>
      <path d="M628 756 V800 H452"/>

      <!-- outer loops -->
      <path d="M762 508 H798 M762 618 H798 M762 728 H798"/>
      <path d="M798 508 V918" marker-end="url(#arrow)"/>
      <path d="M80 920 V508 H134" marker-end="url(#arrow)"/>
      <path d="M80 618 H134" marker-end="url(#arrow)"/>
      <path d="M80 728 H134" marker-end="url(#arrow)"/>

      <rect x="307" y="847" width="290" height="42"/>
      <text x="452" y="876" text-anchor="middle" font-size="22" font-weight="600" letter-spacing="6" stroke="none">REMARKETING</text>
      <path d="M452 889 V918" marker-end="url(#arrow)"/>

      <rect x="63" y="920" width="833" height="48"/>
      <g font-size="13" font-weight="500" stroke="none" text-anchor="middle">
        <text x="135" y="940" fill="#fff">MARKETING</text>
        <text x="135" y="957" fill="#fff">COURRIEL</text>
        <text x="290" y="949" fill="#fff">BLOGUE</text>
        <text x="445" y="949" fill="#fff">RECIBLAGE</text>
        <text x="605" y="949" fill="#fff">MÉDIAS SOCIAUX</text>
        <text x="800" y="940" fill="#fff">AUDIENCES</text>
        <text x="800" y="957" fill="#fff">PERSONNALISÉES</text>
      </g>
      <path d="M205 944 H220 M360 944 H375 M515 944 H530 M690 944 H705"/>
    </svg>
  </div>
</section>

<footer>
  <div class="divider" style="top:3572px"></div>
  <div class="footer"></div>
  <div class="footer-url"><span>www.quorva.ca</span></div>
</footer>

</body>
</html>
```